Natural Immune System Booster

We need a pharmaceutical type box and label design for a vitamin supplement product. Pravolex is in process of being trademarked and should therefore carry the TM symbol. It is comprised of a special blend of over 20 vitamins, herbs and minerals with a High strength vitamin C booster. The tag line should read. The No.1 Natural Support For Your Immune System. Each tube contains 10 tablets. A bar code will be placed on the box carton. We prefer bright and vivid colours, preferably a mix of electric purple, yellow and orange mix. We have three flavours, summer berry (strawberry), tropical fruit and juicy orange - the box and label should indicate the flavours in a creative design element. Effervescent tabelts should be clearly marked on the box and label. The ingredients and instructions should be present on the box outer carton and also the label. We require an eye catching yet simple and bright design that pops off the shelf.
Updates

Target Market(s)

Target customers are male and female 20 - 60+ that live in Western countries that handle household budgets.

Industry/Entity Type

Pharmaceutical

Requirements
Must have
• Please see current box design, all necessary elements and specifications are included here. We require same to be placed on new design.

I have attached a txt file of the supplement facts and other details that are required for both the label and the box

```html
<!DOCTYPE html>
<html lang="en">
<head>
<meta charset="utf-8">
<title>Pravolex Effervescent Tablets – Tube Label</title>
<link href="https://fonts.googleapis.com/css2?family=Arimo:ital,wght@0,400;0,700;1,700&family=Exo+2:ital,wght@1,800&display=swap" rel="stylesheet">
<style>
  :root{
    --stage:#d6d6d6;
    --orange:#f26a1b;
    --orange-light:#f9a13a;
    --yellow:#ffd21a;
    --red:#d7261e;
    --red-dark:#a3140f;
    --silver-1:#f4f4f4;
    --silver-2:#b9b9b9;
    --silver-3:#8d8d8d;
    --ink:#1b1b1b;
    --logo:#3a3a3a;
    --panel-dark:#2a2a2a;
    --white:#ffffff;
  }
  *{box-sizing:border-box;margin:0;padding:0}
  html,body{width:1200px;height:945px;overflow:hidden;background:var(--stage)}
  body{position:relative;font-family:"Arimo",Arial,sans-serif;color:var(--ink)}

  .label{position:absolute;left:50px;top:53px;width:1100px;height:838px;overflow:hidden;background:var(--silver-2)}
  .edge{position:absolute;top:0;bottom:0;width:45px;background:linear-gradient(180deg,var(--orange-light),var(--orange) 50%,#e0520f)}
  .edge--left{left:0}
  .edge--right{right:0;width:40px}

  /* supplement facts */
  .facts{position:absolute;left:45px;top:0;width:1015px;height:160px;background:var(--white);padding:42px 14px 0 20px;display:grid;grid-template-columns:150px 270px 290px 1fr;column-gap:14px;font-size:10px;line-height:1.25}
  .facts__title{font-weight:700;font-size:20px;line-height:1;letter-spacing:.5px}
  .facts__serving{margin-top:6px;font-size:10px}
  .facts__serving b{font-size:11px}
  .facts__col{border-top:3px solid var(--ink)}
  .facts__head{display:flex;justify-content:space-between;font-weight:700;font-size:9px;border-bottom:1px solid var(--ink);padding:1px 0}
  .facts__row{display:flex;justify-content:space-between;border-bottom:1px solid #999;padding:1px 0}
  .facts__row--sub{padding-left:14px}
  .facts__row b{font-weight:700}
  .facts__vitamins{position:absolute;left:190px;top:141px;width:580px;display:flex;justify-content:space-between;font-size:9px;border-top:2px solid var(--ink);padding-top:2px}
  .facts__note{font-size:8px;line-height:1.2;color:#333}
  .facts__note table{margin-top:4px;border-collapse:collapse;width:100%;font-size:7.5px}
  .facts__note td{padding:0 2px;border-bottom:1px solid #bbb}

  /* herbal blend strip */
  .blend{position:absolute;left:45px;top:160px;width:1015px;height:72px;background:linear-gradient(90deg,var(--red-dark),var(--red) 20%,var(--red) 80%,var(--red-dark));color:var(--white);padding:10px 20px;display:grid;grid-template-columns:230px 250px 260px 1fr;gap:12px;font-size:11px;line-height:1.3}
  .blend b{font-weight:700}

  /* main face */
  .face{position:absolute;left:45px;top:232px;width:1015px;height:446px;background:linear-gradient(180deg,var(--silver-3) 0%,var(--silver-1) 38%,var(--silver-2) 70%,var(--silver-3) 100%)}
  .face__graphic{position:absolute;left:40px;top:30px;width:960px;height:330px;border-radius:50%;
    background:radial-gradient(ellipse at 50% 50%,var(--red) 0%,#ea4d1c 35%,var(--orange) 55%,var(--yellow) 72%,rgba(255,210,26,0) 100%)}
  .face__kicker{position:absolute;left:55px;top:92px;font-family:"Exo 2","Arimo",sans-serif;font-style:italic;font-weight:800;font-size:40px;letter-spacing:1px;color:var(--yellow);-webkit-text-stroke:1px var(--red-dark);text-transform:uppercase}
  .face__brand{position:absolute;left:55px;top:128px;font-family:"Arimo",Arial,sans-serif;font-weight:700;font-size:128px;line-height:1;letter-spacing:-2px;color:var(--logo)}
  .face__tm{position:absolute;left:852px;top:170px;width:46px;height:46px;border:3px solid var(--logo);border-radius:50%;display:flex;align-items:center;justify-content:center;font-weight:700;font-size:17px;color:var(--logo)}
  .face__tagline{position:absolute;left:55px;top:268px;font-weight:700;font-style:italic;font-size:33px;color:var(--red);-webkit-text-stroke:5px var(--white);paint-order:stroke fill;white-space:nowrap}
  .face__count{position:absolute;left:401px;top:328px;width:187px;height:60px;border-radius:50%;background:radial-gradient(ellipse at 50% 35%,#fff27a,var(--yellow) 55%,#f0a800);border:3px solid var(--red-dark);display:flex;align-items:center;justify-content:center;font-weight:700;font-style:italic;font-size:22px;color:var(--red)}

  /* back panel */
  .info{position:absolute;left:45px;top:678px;width:1015px;height:160px;background:var(--panel-dark);color:var(--white);padding:10px 20px;font-size:12px;line-height:1.2}
  .info p{margin-bottom:6px}
  .info p:last-child{margin-bottom:0}
  .info__heading{font-weight:700;display:block}
</style>
</head>
<body>
<div class="label">
  <div class="edge edge--left"></div>
  <div class="edge edge--right"></div>

  <section class="facts" aria-label="Supplement facts">
    <div>
      <div class="facts__title">SUPPLEMENT<br>FACTS</div>
      <div class="facts__serving">Serving Size 45 grams<br>Serving Per Container 1<br><b>Calories</b> 155</div>
    </div>
    <div class="facts__col">
      <div class="facts__head"><span>Amount Per Serving</span><span>% Daily Values*</span></div>
      <div class="facts__row"><span><b>Total Fat</b> 10g</span><b>20%</b></div>
      <div class="facts__row facts__row--sub"><span>Saturated Fat 0.5g</span><b>15%</b></div>
      <div class="facts__row facts__row--sub"><span>Trans Fat 0g</span><span></span></div>
      <div class="facts__row"><span><b>Cholesterol</b> 0mg</span><b>0%</b></div>
      <div class="facts__row"><span><b>Potassium</b> 110mg</span><b>3%</b></div>
    </div>
    <div class="facts__col">
      <div class="facts__head"><span>Amount Per Serving</span><span>% Daily Values*</span></div>
      <div class="facts__row"><span><b>Sodium</b> 0mg</span><b>0%</b></div>
      <div class="facts__row"><span><b>Total Carbohydrate</b> 30g</span><b>7%</b></div>
      <div class="facts__row facts__row--sub"><span>Dietary Fiber 4g</span><b>16%</b></div>
      <div class="facts__row facts__row--sub"><span>Sugars 6g</span><span></span></div>
      <div class="facts__row"><span><b>Protein</b> 0g</span><b>0%</b></div>
    </div>
    <div class="facts__note">
      * Percent Daily Values are based on a 2,000 calorie diet. Your values may be higher or lower depending on your calorie needs.
      <table>
        <tr><td></td><td>Calories</td><td>2,000</td></tr>
        <tr><td>Total Fat</td><td>Less than</td><td>65g</td></tr>
        <tr><td>Sat Fat</td><td>Less than</td><td>20g</td></tr>
        <tr><td>Cholesterol</td><td>Less than</td><td>300mg</td></tr>
        <tr><td>Sodium</td><td>Less than</td><td>2400mg</td></tr>
        <tr><td>Total Carbs</td><td></td><td>300g</td></tr>
      </table>
    </div>
    <div class="facts__vitamins"><span>Vitamin A 2%</span><span>•</span><span>Vitamin C 0%</span><span>•</span><span>Calcium 0%</span><span>•</span><span>Iron 11%</span></div>
  </section>

  <section class="blend" aria-label="Proprietary blends">
    <div><b>PROPRIETARY HERBAL BLEND</b><br>(400mg*)<br>Lonicera Japonica (Flower)<br>Forsythia Suspensa (Fruit)</div>
    <div>Schizonepeta Tenuifolia (Aerial)<br>Hydrastis Canadensis (Aerial)<br>Ginger (Root)<br>Chinese Vitex (Fruit) Isatis (Root)</div>
    <div>Ganoderma Lucidum<br>Astragalus<br>Echinacea purpurea (Aerial)<br>Panax notoginseng</div>
    <div><b>Proprietary Amino Acid Blend</b><br>(50mg*)<br>Glutamine as (L-Glutamine)<br>Lysine as (L-Lysine HCl)</div>
  </section>

  <section class="face">
    <div class="face__graphic" role="img" aria-label="Orange, red and yellow swoosh graphic behind the product name"></div>
    <div class="face__kicker">Effervescent Tablets</div>
    <div class="face__brand">Pravolex</div>
    <div class="face__tm">TM</div>
    <div class="face__tagline">The No.1 Natural Support For Your Immune System*</div>
    <div class="face__count">10 tablets</div>
  </section>

  <section class="info">
    <p><span class="info__heading">OTHER INGREDIENT:</span>Sucrose, Maltodextrin, Citric acid, Artificial Flavor, Sucralose, Natural Color.</p>
    <p>*Daily value not established. Percent Daily values are based on a 2000 calorie diet. Other ingredients: Sucrose, Maltodextrin, Citric Acid, Artificial Flavor, Stevioside, Natural Color.</p>
    <p><b>Directions:</b> For adults and children 12 years and older. Place one tablet in 5 - 7 fl oz of water. Allow to dissolve and drink. Repeat every 4-5hrs daily as necessary up to three times per day. Do not take if pregnant, breast feeding on medication or with a known medical condition unless you have permission from your doctor.</p>
    <p><b>Distributed by:</b> Pravolex LLC, 2240 Harbor Lane, 40112, County of Marlow, USA<br>Questions? Email: info@pravolex.com &nbsp;web: www.pravolex.com &nbsp;tel: 1-800-555-0148</p>
  </section>
</div>
</body>
</html>
```